Biz card & Stationary
Hollin Ridge Materials
Modern
Dana Wexler
Sales Manager
48217 Quimby Lane
P. O. Box 5179
Doswell, VA 24619
dwexler@lumarbo.com
www.lumarbo.com

```html
<!DOCTYPE html>
<html lang="en">
<head>
<meta charset="utf-8">
<title>Hollin Ridge Materials — Stationery Set</title>
<link href="https://fonts.googleapis.com/css2?family=Open+Sans:wght@400;600&family=Roboto+Condensed:wght@700&display=swap" rel="stylesheet">
<style>
  :root{
    --stage:#000000;
    --paper:#ffffff;
    --navy:#17396f;
    --blue:#2a6fc0;
    --blue-light:#4d8fd8;
    --ink:#3a3f48;
    --muted:#8a9099;
    --rule:#d7dbe1;
    --faint:#eef0f3;
    --slate:#2b2f35;
  }
  *{box-sizing:border-box;margin:0;padding:0}
  html,body{width:1200px;height:899px;overflow:hidden;background:var(--stage)}
  body{position:relative;font-family:"Open Sans",Arial,sans-serif;color:var(--ink)}

  .sheet{position:absolute;background:var(--paper);overflow:hidden;box-shadow:0 4px 14px rgba(255,255,255,.06)}

  /* brand lockup */
  .brand{display:flex;align-items:center;gap:6px}
  .brand-dot{width:22px;height:22px;border-radius:50%;background:var(--navy);flex:none}
  .brand-name{font-family:"Roboto Condensed",Arial,sans-serif;font-weight:700;color:var(--navy);
    text-transform:uppercase;font-size:10px;line-height:1.05;letter-spacing:.3px}
  .brand--light .brand-dot{background:var(--paper)}
  .brand--light .brand-name{color:var(--paper)}

  .faint-disc{position:absolute;border-radius:50%;background:var(--faint)}

  .footer-band{position:absolute;left:0;right:0;bottom:0;height:14px;
    background:linear-gradient(90deg,var(--navy),var(--blue));
    color:var(--paper);font-size:6px;display:flex;align-items:center;justify-content:flex-end;padding-right:12px;letter-spacing:.6px}
  .contact{font-size:6px;line-height:1.5;color:var(--muted)}

  /* letterhead */
  .letterhead{left:40px;top:40px;width:300px;height:424px}
  .letterhead .brand{position:absolute;left:22px;top:24px}
  .letterhead .contact{position:absolute;right:22px;top:24px;text-align:right}
  .letter-body{position:absolute;left:22px;right:22px;top:90px;font-size:6.5px;line-height:1.7;color:var(--ink)}
  .letter-body p{margin-bottom:8px}
  .signature{margin-top:14px;width:60px;height:1px;background:var(--muted)}
  .letterhead .faint-disc{width:150px;height:150px;right:-20px;bottom:50px}

  /* fax */
  .fax{left:370px;top:40px;width:300px;height:424px}
  .fax .brand{position:absolute;left:22px;top:24px}
  .fax-title{position:absolute;right:22px;top:22px;font-family:"Roboto Condensed",Arial,sans-serif;font-weight:700;font-size:22px;color:var(--navy);letter-spacing:2px}
  .fax-fields{position:absolute;left:22px;right:22px;top:70px;border-top:1px solid var(--rule)}
  .fax-row{display:flex;border-bottom:1px solid var(--rule);height:20px;align-items:center;font-size:7px}
  .fax-row span{width:60px;color:var(--navy);font-weight:600}
  .fax-checks{position:absolute;left:22px;top:205px;display:flex;gap:18px;font-size:7px}
  .fax-checks label{display:flex;align-items:center;gap:4px}
  .fax-checks i{width:7px;height:7px;border:1px solid var(--muted);display:block}
  .fax .faint-disc{width:150px;height:150px;left:75px;top:250px}
  .fax .contact{position:absolute;left:22px;bottom:24px}

  /* envelope back */
  .envelope-back{left:700px;top:40px;width:460px;height:230px}
  .envelope-back svg{position:absolute;left:0;top:0}
  .envelope-back .brand{position:absolute;left:218px;top:118px}

  /* envelope front */
  .envelope-front{left:700px;top:290px;width:460px;height:174px}
  .envelope-front .brand{position:absolute;left:22px;top:20px}
  .envelope-front .contact{position:absolute;left:50px;top:48px}
  .envelope-front .faint-disc{width:120px;height:120px;right:30px;top:10px}

  /* cards */
  .card{width:260px;height:150px}
  .card-front{left:40px;top:500px}
  .card-front .brand{position:absolute;left:16px;top:16px}
  .card-person{position:absolute;left:16px;bottom:22px}
  .card-person strong{display:block;font-family:"Roboto Condensed",Arial,sans-serif;font-weight:700;font-size:12px;color:var(--navy);text-transform:uppercase}
  .card-person em{font-style:normal;font-size:7px;color:var(--muted)}
  .card-front .contact{position:absolute;right:16px;bottom:22px;text-align:right}
  .card-front .footer-band{height:8px}

  .card-back-blue{left:320px;top:500px;background:linear-gradient(135deg,var(--navy),var(--blue-light))}
  .card-back-dark{left:600px;top:500px;background:var(--slate)}
  .card-back-blue .brand,.card-back-dark .brand{position:absolute;left:50%;top:50%;transform:translate(-50%,-50%)}
  .card-back-dark .web{position:absolute;left:0;right:0;bottom:14px;text-align:center;font-size:6px;color:var(--muted);letter-spacing:1px}

  .card-small{left:880px;top:500px}
  .card-small .brand{position:absolute;left:16px;top:16px}
  .card-small .card-person{left:16px;bottom:24px}
  .card-small .footer-band{height:8px}
</style>
</head>
<body>

<!-- Letterhead -->
<section class="sheet letterhead">
  <div class="brand"><span class="brand-dot"></span><span class="brand-name">Hollin Ridge<br>Materials</span></div>
  <div class="contact">48217 Quimby Lane<br>P. O. Box 5179<br>Doswell, VA 24619<br>Tel (804) 555-0142</div>
  <div class="faint-disc"></div>
  <div class="letter-body">
    <p>Dear Client,</p>
    <p>Thank you for choosing us for your next building project. Our team will follow up with pricing and delivery details this week.</p>
    <p>Please call us with any questions about materials or scheduling.</p>
    <p>Sincerely,</p>
    <div class="signature"></div>
    <p>Dana Wexler<br>Sales Manager</p>
  </div>
  <div class="footer-band">www.lumarbo.com</div>
</section>

<!-- Fax cover -->
<section class="sheet fax">
  <div class="brand"><span class="brand-dot"></span><span class="brand-name">Hollin Ridge<br>Materials</span></div>
  <div class="fax-title">FAX</div>
  <div class="fax-fields">
    <div class="fax-row"><span>To</span></div>
    <div class="fax-row"><span>From</span></div>
    <div class="fax-row"><span>Fax</span></div>
    <div class="fax-row"><span>Phone</span></div>
    <div class="fax-row"><span>Date</span></div>
    <div class="fax-row"><span>Pages</span></div>
  </div>
  <div class="fax-checks">
    <label><i></i>Urgent</label>
    <label><i></i>Review</label>
    <label><i></i>Reply</label>
  </div>
  <div class="faint-disc"></div>
  <div class="contact">48217 Quimby Lane · P. O. Box 5179 · Doswell, VA 24619 · Tel (804) 555-0142</div>
  <div class="footer-band">www.lumarbo.com</div>
</section>

<!-- Envelope back -->
<section class="sheet envelope-back">
  <svg width="460" height="230" viewBox="0 0 460 230" aria-hidden="true">
    <defs>
      <linearGradient id="flapBlue" x1="0" y1="0" x2="0" y2="1">
        <stop offset="0" stop-color="#17396f"/>
        <stop offset="1" stop-color="#2a6fc0"/>
      </linearGradient>
    </defs>
    <polygon points="0,0 460,0 230,110" fill="url(#flapBlue)"/>
    <polyline points="0,230 200,120" fill="none" stroke="#d7dbe1" stroke-width="1"/>
    <polyline points="460,230 260,120" fill="none" stroke="#d7dbe1" stroke-width="1"/>
  </svg>
  <div class="brand"><span class="brand-dot"></span></div>
</section>

<!-- Envelope front -->
<section class="sheet envelope-front">
  <div class="brand"><span class="brand-dot"></span><span class="brand-name">Hollin Ridge<br>Materials</span></div>
  <div class="contact">48217 Quimby Lane<br>P. O. Box 5179<br>Doswell, VA 24619</div>
  <div class="faint-disc"></div>
  <div class="footer-band">www.lumarbo.com</div>
</section>

<!-- Business card front -->
<section class="sheet card card-front">
  <div class="brand"><span class="brand-dot"></span><span class="brand-name">Hollin Ridge<br>Materials</span></div>
  <div class="card-person"><strong>Dana Wexler</strong><em>Sales Manager</em></div>
  <div class="contact">48217 Quimby Lane<br>P. O. Box 5179<br>Doswell, VA 24619<br>Tel (804) 555-0142<br>Cell (804) 555-0187<br>dwexler@lumarbo.com</div>
  <div class="footer-band"></div>
</section>

<!-- Business card back, blue -->
<section class="sheet card card-back-blue">
  <div class="brand brand--light"><span class="brand-dot"></span><span class="brand-name">Hollin Ridge<br>Materials</span></div>
</section>

<!-- Business card back, dark -->
<section class="sheet card card-back-dark">
  <div class="brand brand--light"><span class="brand-dot"></span></div>
  <div class="web">www.lumarbo.com</div>
</section>

<!-- Small card -->
<section class="sheet card card-small">
  <div class="brand"><span class="brand-dot"></span><span class="brand-name">Hollin Ridge<br>Materials</span></div>
  <div class="card-person"><strong>Dana Wexler</strong><em>dwexler@lumarbo.com</em></div>
  <div class="footer-band"></div>
</section>

</body>
</html>
```